Update Letterhead for Harbor Vale Advisors

We need a modernized and updated letterhea. We DO NOT want to change fonts, we want incorporate the logo and words better and make a sleeker and elegant logo catering to wealthy clients. Harbor is a wealth management firm catering to business owners, physicians, and high net wort clientele. Our letterhead should have strength and elegance and cater to that market. Guaranteed payment.

Requirements
Must have
• PLEASE NOTE THAT THE LOGO USED IN THE ORIGINAL DESIGNS ARE INCORRECT! Please update to the new logo!
• We also changed our color scheme to grey and gold and black. Please refer to website www.harborva-example.com to see what I mean as we want to update to that rather than the dark blue. (Most likely grey and gold)

```html
<!DOCTYPE html>
<html lang="en">
<head>
<meta charset="utf-8">
<title>Harbor Vale Advisors — Letterhead</title>
<link rel="stylesheet" href="https://fonts.googleapis.com/css2?family=Cinzel:wght@700&family=Libre+Baskerville:wght@700&family=Arimo&display=swap">
<style>
  :root {
    --backdrop: #efece6;
    --paper: #ffffff;
    --gold: #d4b06a;
    --grey: #6d6e71;
    --rule: #77787b;
    --band-grey: #6e6f71;
    --white: #ffffff;
  }
  * { box-sizing: border-box; margin: 0; padding: 0; }
  html, body {
    width: 1200px;
    height: 1200px;
    overflow: hidden;
    background: var(--backdrop);
  }
  .letterhead {
    position: absolute;
    left: 156px;
    top: 28px;
    width: 887px;
    height: 1147px;
    background: var(--paper);
    box-shadow: 0 2px 10px rgba(0,0,0,0.12);
    overflow: hidden;
  }
  .header-band {
    position: absolute;
    left: 0; top: 0;
    width: 100%;
    height: 152px;
    background: var(--gold);
  }
  .header-band svg {
    position: absolute;
    left: 0; top: 0;
  }
  .wordmark {
    position: absolute;
    left: 0;
    top: 156px;
    width: 100%;
    text-align: center;
    font-family: "Cinzel", serif;
    font-weight: 700;
    color: var(--grey);
    line-height: 1;
  }
  .wordmark-main {
    display: block;
    font-size: 40px;
    letter-spacing: 0.5px;
  }
  .wordmark-sub {
    display: block;
    margin-top: 9px;
    font-size: 25px;
    letter-spacing: 1px;
  }
  .rule {
    position: absolute;
    height: 3px;
    background: var(--rule);
  }
  .rule-head-left  { left: 0;     top: 227px; width: 345px; }
  .rule-head-right { left: 540px; top: 227px; width: 347px; }
  .rule-mission-left  { left: 2px;   top: 1042px; width: 288px; }
  .rule-mission-right { left: 605px; top: 1042px; width: 282px; }
  .mission-heading {
    position: absolute;
    left: 0;
    top: 1032px;
    width: 100%;
    text-align: center;
    font-family: "Libre Baskerville", serif;
    font-weight: 700;
    font-size: 16px;
    color: var(--gold);
    line-height: 22px;
  }
  .mission-band {
    position: absolute;
    left: 0;
    top: 1076px;
    width: 100%;
    height: 71px;
    background: var(--band-grey);
    display: flex;
    align-items: center;
    justify-content: center;
  }
  .mission-text {
    font-family: "Arimo", sans-serif;
    font-size: 16.5px;
    line-height: 22px;
    color: var(--white);
    text-align: center;
    text-transform: uppercase;
  }
</style>
</head>
<body>
  <div class="letterhead">
    <div class="header-band">
      <svg width="887" height="152" viewBox="0 0 887 152" aria-hidden="true">
        <circle cx="443" cy="136" r="121" fill="none" stroke="var(--white)" stroke-width="2.5"/>
      </svg>
    </div>

    <div class="wordmark">
      <span class="wordmark-main">HARBOR VALE</span>
      <span class="wordmark-sub">ADVISORS</span>
    </div>
    <div class="rule rule-head-left"></div>
    <div class="rule rule-head-right"></div>

    <div class="rule rule-mission-left"></div>
    <div class="rule rule-mission-right"></div>
    <h2 class="mission-heading">OUR MISSION STATEMENT</h2>

    <div class="mission-band">
      <p class="mission-text">“We empower our clients to realize financial independence by securing<br>today, tomorrow and the future.&nbsp; One family, one solution, and one legacy at a time.”</p>
    </div>
  </div>
</body>
</html>
```